Neighbourhood assistance

I need an app design for a social idea. Each person has some skils and could offer some assistance to some of his neighbours. With this app I will bring people together. For free or also for some money.That doesn't matter.

Please have a look into my pptx file which should give you an idea about the upcoming app.

Social

```html
<!DOCTYPE html>
<html lang="de">
<head>
<meta charset="utf-8">
<title>Angebote für Hütedienst</title>
<link rel="stylesheet" href="https://fonts.googleapis.com/css2?family=Dosis:wght@500&family=Raleway:wght@400;500&family=Inter:wght@500;600&display=swap">
<style>
  :root {
    --violet: #9a10c0;
    --violet-dark: #7c0598;
    --white: #ffffff;
    --mint: #0bd18a;
    --field-line: rgba(255,255,255,0.55);
    --photo-light: #f3ece6;
    --photo-mid: #b07a55;
    --photo-dark: #5a3320;
  }
  * { margin: 0; padding: 0; box-sizing: border-box; }
  html, body { width: 676px; height: 1200px; overflow: hidden; }
  body {
    position: relative;
    background: var(--violet);
    color: var(--white);
    font-family: "Raleway", sans-serif;
  }
  .status-bar {
    position: absolute; left: 0; top: 0; width: 676px; height: 42px;
    font-family: "Inter", sans-serif; font-weight: 600; font-size: 23px;
  }
  .status-bar .signal { position: absolute; left: 15px; top: 14px; }
  .status-bar .carrier { position: absolute; left: 101px; top: 7px; }
  .status-bar .wifi { position: absolute; left: 172px; top: 10px; }
  .status-bar .clock { position: absolute; left: 0; width: 676px; top: 7px; text-align: center; }
  .status-bar .lock { position: absolute; left: 503px; top: 10px; }
  .status-bar .battery-level { position: absolute; left: 540px; top: 7px; }
  .status-bar .battery { position: absolute; left: 614px; top: 11px; }

  .app-header {
    position: absolute; left: 0; top: 42px; width: 676px; height: 90px;
    background: var(--violet-dark);
  }
  .back-button {
    position: absolute; left: 18px; top: 30px; width: 77px; height: 38px;
    background: var(--white); color: var(--violet);
    font-size: 17px; line-height: 38px; text-align: center;
  }
  .screen-title {
    position: absolute; left: 121px; top: 20px;
    font-family: "Dosis", sans-serif; font-weight: 500; font-size: 39px;
    letter-spacing: 0.5px; line-height: 50px;
  }

  .view-switch {
    position: absolute; left: 104px; top: 162px; width: 492px; height: 44px;
    border: 1px solid var(--white); display: flex;
    font-size: 29px;
  }
  .view-switch span { flex: 1; text-align: center; line-height: 40px; }
  .view-switch .active { background: var(--white); color: var(--violet); }

  .provider-title {
    position: absolute; left: 0; width: 644px; top: 262px;
    text-align: center; font-size: 28px;
  }
  .field {
    position: absolute; height: 36px; width: 217px;
    border: 1px solid var(--field-line);
    font-size: 16px; line-height: 34px; padding-left: 26px;
  }
  .field-name { left: 67px; top: 336px; }
  .field-firstname { left: 361px; top: 334px; }

  .avatar {
    position: absolute; left: 240px; top: 449px; width: 180px; height: 180px;
    border-radius: 50%;
    background: radial-gradient(circle at 55% 45%, var(--photo-light) 0 30%, var(--photo-mid) 55%, var(--photo-dark) 80%);
  }

  .action {
    position: absolute; height: 85px; width: 482px;
    background: var(--mint); border-radius: 2px;
    font-size: 29px; line-height: 85px; text-align: center;
  }
  .action-contact { left: 113px; top: 737px; }
  .action-restart { left: 112px; top: 843px; }
</style>
</head>
<body>
  <div class="status-bar">
    <svg class="signal" width="76" height="14" viewBox="0 0 76 14" fill="#fff">
      <circle cx="6" cy="7" r="6"/><circle cx="21" cy="7" r="6"/><circle cx="36" cy="7" r="6"/><circle cx="51" cy="7" r="6"/>
      <circle cx="66" cy="7" r="5.2" fill="none" stroke="#fff" stroke-width="1.5"/>
    </svg>
    <span class="carrier">Velo</span>
    <svg class="wifi" width="26" height="20" viewBox="0 0 26 20" fill="none" stroke="#fff" stroke-width="3" stroke-linecap="round">
      <path d="M2 7a16 16 0 0 1 22 0"/><path d="M6 11a10 10 0 0 1 14 0"/><circle cx="13" cy="16" r="2" fill="#fff" stroke="none"/>
    </svg>
    <span class="clock">4:20 PM</span>
    <svg class="lock" width="24" height="24" viewBox="0 0 24 24" fill="none" stroke="#fff" stroke-width="2">
      <path d="M20 12a8 8 0 1 1-3-6.2"/><rect x="8.5" y="11" width="7" height="6" fill="#fff" stroke="none"/><path d="M10 11V9a2 2 0 0 1 4 0v2"/>
    </svg>
    <span class="battery-level">100%</span>
    <svg class="battery" width="50" height="22" viewBox="0 0 50 22">
      <rect x="1" y="1" width="44" height="20" rx="3" fill="none" stroke="#fff" stroke-width="2"/>
      <rect x="4" y="4" width="38" height="14" rx="1" fill="#fff"/>
      <rect x="46" y="7" width="3" height="8" rx="1" fill="#fff"/>
    </svg>
  </div>

  <header class="app-header">
    <div class="back-button">Back</div>
    <h1 class="screen-title">ANGEBOTE FÜR HÜTEDIENST</h1>
  </header>

  <nav class="view-switch">
    <span class="active">Liste</span>
    <span>Karte</span>
  </nav>

  <h2 class="provider-title">Anbieter 1</h2>
  <div class="field field-name">Name</div>
  <div class="field field-firstname">Vorname</div>

  <div class="avatar" role="img" aria-label="Profilfoto des Anbieters"></div>

  <div class="action action-contact">Kontaktieren</div>
  <div class="action action-restart">Neu starten</div>
</body>
</html>
```